Flyer for Leaflet Dropping - A5 - Managed IT Support Flyer

I need an A5 double sided flyer LANDSCAPE - design for door to door leaflet dropping / marketing to local businesses.
Our main aim is to promote our ‘Managed IT Support’ services to local small and medium businesses.
Our secondary aim is to promote our additional services which are internet/communications and cloud services. We want to mention these services but they are only secondary therefore need to take a smaller focus and not detract from the main message of the flyer.
• Hosted Cloud Desktop
• VOIP Telephone Systems
• Nimbora 365
• Cloud Services
• Internet Services
• Disaster Recovery

Target Market(s)

Our target audience is senior members of company (MD, FD, Owners, Operations, Management), looking to outsource their IT requirements/needs. UK Only. N London

Industry/Entity Type

Information Technology

Font styles to use
Sans Serif

Requirements
Must have
• Please use the website for a source of information and inspiration – www.brimtek.co.uk.
• We specifically feel the points below are important and want to see them feature.
• 1. Large bold heading highlighting our primary service ‘Managed IT Support’
• 2. Secondary sub-heading explaining exactly what we do.
• ‘We manage your IT ensuring systems are monitored, supported and protected to enhance business growth.’
• 3. Reasons to choose BrimTek – take inspiration from https://www.brimtek.co.uk/about-us/
• 4. No Risk - Our 90 Day Satisfaction Guarantee (see website).
• 5. Areas we cover: ‘Trusted by 100+ businesses across Hertfordshire, Essex, London & beyond.‘
• 6. Name of company, contact details.
• CALL TO ACTION
• 1. Call Us – 03339017462
• 2. Visit our Website – https://www.brimtek.co.uk/gomanaged

```html
<!DOCTYPE html>
<html lang="en">
<head>
<meta charset="utf-8">
<title>BrimTek – Managed IT Support Flyer</title>
<link rel="stylesheet" href="https://fonts.googleapis.com/css2?family=Montserrat:wght@300;400;500;700&family=Oswald:wght@500;600&family=Fira+Sans:wght@400;600;700&display=swap">
<style>
:root{
  --backdrop:#bbbcbe;
  --paper:#ffffff;
  --blue:#3b9ad6;
  --grey-head:#5f6166;
  --ink:#2b2b2d;
  --muted:#8a8c90;
  --green:#7cc14a;
  --purple:#9b6fb7;
  --red:#ec5f63;
  --slate:#616164;
}
*{margin:0;padding:0;box-sizing:border-box}
html,body{width:914px;height:1200px;overflow:hidden}
body{background:var(--backdrop);font-family:"Montserrat",sans-serif;color:var(--ink);position:relative}
.side{position:absolute;left:104px;width:706px;height:498px;background:var(--paper);overflow:hidden}
.side-front{top:92px}
.side-back{top:642px}
.brand{position:absolute;left:38px;top:24px;display:flex;align-items:center;gap:10px}
.brand-dot{width:42px;height:42px;border-radius:50%;background:var(--blue)}
.brand-name{font-size:29px;font-weight:500;color:var(--grey-head);line-height:1}
.brand-tag{font-size:10px;color:var(--muted);margin-top:3px}
.headline{position:absolute;right:22px;top:20px;font-family:"Oswald",sans-serif;font-weight:600;font-size:44px;letter-spacing:-1px;line-height:1.05}
.headline .accent{color:var(--blue)}
.headline .plain{color:var(--grey-head)}
.photo{position:absolute;left:0;width:349px}
.photo-office{top:80px;height:218px;background:linear-gradient(135deg,#e8e9ea 0%,#c7ccd1 55%,#a9a29a 100%)}
.photo-meeting{top:89px;height:213px;background:linear-gradient(135deg,#a5705a 0%,#c9b8a4 50%,#6b6f75 100%)}
.intro{position:absolute;left:349px;top:80px;width:357px;height:218px;background:var(--blue);color:#fff;padding:20px 34px}
.intro-lead{font-size:18.5px;line-height:24px;font-weight:400}
.intro-rule{height:1px;background:rgba(255,255,255,.45);margin:14px 0 10px}
.intro-area{font-size:13px;line-height:18px;font-weight:300}
.reasons{position:absolute;left:0;top:298px;width:706px;height:91px;display:flex}
.reason{position:relative;flex:1;color:#fff;text-align:center;padding:22px 22px 0;font-family:"Fira Sans",sans-serif}
.reason-fast{background:var(--green)}
.reason-accredited{background:var(--purple)}
.reason-years{background:var(--red)}
.reason-badge{position:absolute;left:50%;top:-28px;transform:translateX(-50%);width:44px;height:44px;border-radius:50%;border:2px solid #fff;display:flex;align-items:center;justify-content:center}
.reason-fast .reason-badge{background:var(--green)}
.reason-accredited .reason-badge{background:var(--purple)}
.reason-years .reason-badge{background:var(--red)}
.reason-title{font-size:15px;font-weight:600;margin-bottom:4px}
.reason-text{font-size:10px;line-height:12.5px;text-align:justify;text-align-last:left}
.reason-text b{font-weight:700}
.contact-call{position:absolute;left:38px;top:412px}
.call-label{font-size:16px;color:var(--muted);font-weight:400;letter-spacing:.3px}
.call-number{display:flex;align-items:center;gap:4px;font-size:25px;font-weight:400;color:var(--ink);letter-spacing:.4px}
.divider{position:absolute;top:410px;width:1px;height:48px;background:#c9cacc}
.address{position:absolute;left:269px;top:406px;font-size:12.5px;line-height:17px;color:#4a4b4e}
.guarantee{position:absolute;left:490px;top:406px}
.guarantee-head{font-family:"Montserrat",sans-serif;font-weight:700;font-size:23px;color:var(--blue);line-height:1}
.guarantee-text{font-family:"Fira Sans",sans-serif;font-weight:700;font-size:13.5px;line-height:15.5px;color:var(--ink);margin-top:3px}
.seal{position:absolute;left:607px;top:403px}
.url-bar{position:absolute;left:0;top:469px;height:29px;background:var(--blue);color:#fff;font-size:12.5px;letter-spacing:2px;padding:7px 0 0 40px}
.side-front .url-bar{width:355px}
.side-back .url-bar{width:346px}
.headline-services{font-family:"Oswald",sans-serif;font-weight:500;font-size:36px;letter-spacing:4px;top:26px;right:58px}
.headline-services .plain{color:#222}
.summary{position:absolute;left:39px;top:318px;width:290px;font-size:11px;line-height:16px;color:var(--ink);white-space:nowrap}
.side-back .contact-call{left:45px;top:366px}
.side-back .address{left:40px;top:435px;font-size:12px;line-height:16.5px}
.services{position:absolute;left:349px;top:89px;width:357px;height:378px;background:var(--slate);color:#fff;padding:8px 36px 0 41px}
.service{height:70px}
.service-name{font-size:19px;font-weight:400;line-height:24px}
.service-text{font-size:12px;line-height:17px;font-weight:400;color:#f1f1f1}
.service-icon{position:absolute;left:332px;width:34px;height:34px;border-radius:50%;background:#fff;border:1.5px solid #b9babd;display:flex;align-items:center;justify-content:center}
</style>
</head>
<body>

<section class="side side-front">
  <div class="brand">
    <span class="brand-dot"></span>
    <div>
      <div class="brand-name">BrimTek</div>
      <div class="brand-tag">Helping you work smarter</div>
    </div>
  </div>
  <h1 class="headline"><span class="accent">MANAGED</span> <span class="plain">IT SUPPORT</span></h1>

  <div class="photo photo-office" role="img" aria-label="Photo of a smiling support agent wearing a headset at a laptop in a bright open-plan office"></div>

  <div class="intro">
    <p class="intro-lead">We manage your IT ensuring systems are monitored, supported and protected to enhance business growth.</p>
    <div class="intro-rule"></div>
    <p class="intro-area">Trusted by 100+ businesses across Hertfordshire, Essex, London &amp; beyond</p>
  </div>

  <div class="reasons">
    <div class="reason reason-fast">
      <span class="reason-badge">
        <svg width="24" height="24" viewBox="0 0 30 30" fill="none" stroke="#fff" stroke-width="2.6" stroke-linecap="round"><path d="M6 10a11 11 0 1 1-1 7"/><path d="M3 6v5h5"/><path d="M15 9v7l4 3"/></svg>
      </span>
      <div class="reason-title">Fast Response Times</div>
      <p class="reason-text"><b>Super fast</b> service desk with an industry leading average wait time of <b>under 13 seconds</b></p>
    </div>
    <div class="reason reason-accredited">
      <span class="reason-badge">
        <svg width="24" height="24" viewBox="0 0 30 30" fill="none" stroke="#fff" stroke-width="1.8" stroke-linejoin="round"><path d="M15 3l3.6 7.6 8.2 1-6 5.7 1.6 8.2L15 21.5 7.6 25.5l1.6-8.2-6-5.7 8.2-1z"/></svg>
      </span>
      <div class="reason-title">Fully Accredited</div>
      <p class="reason-text">Nimbora <b>Gold</b> Partner, Tier-1 CSP Partner, TechCert Managed Services and Voxline <b>Platinum Partner</b></p>
    </div>
    <div class="reason reason-years">
      <span class="reason-badge">
        <svg width="24" height="24" viewBox="0 0 30 30" fill="none" stroke="#fff" stroke-width="1.8" stroke-linejoin="round"><rect x="4" y="13" width="5" height="12"/><path d="M9 14l5-8c1-2 4-1 3.5 1.5L16.5 12H24c1.5 0 2.5 1.3 2 2.8l-2.5 8.5c-.3 1-1.2 1.7-2.2 1.7H9"/></svg>
      </span>
      <div class="reason-title">Years of Experince</div>
      <p class="reason-text">We’ve been in business for <b>over 10 years</b> and now support over <b>100+ customers</b></p>
    </div>
  </div>

  <div class="contact-call">
    <div class="call-label">CALL US</div>
    <div class="call-number">
      <svg width="24" height="22" viewBox="0 0 24 22"><path d="M2 8c0-3 4-5 10-5s10 2 10 5l-1 2-4-1V7c-3-1-7-1-10 0v2l-4 1z" fill="#3b9ad6"/><path d="M6 11h12l3 9H3z" fill="#3b9ad6"/><circle cx="12" cy="15" r="2.5" fill="#fff"/></svg>
      03339017462
    </div>
  </div>
  <div class="divider" style="left:249px"></div>
  <p class="address">BrimTek Ltd, Unit 8,<br>Calder Court, Hertford,<br>Hertfordshire, SG14 2QX</p>
  <div class="divider" style="left:465px;top:406px;height:60px"></div>
  <div class="guarantee">
    <div class="guarantee-head">NO RISK</div>
    <div class="guarantee-text">OUR 90 DAY<br>SATISFACTION<br>GUARANTEE</div>
  </div>
  <svg class="seal" width="78" height="78" viewBox="0 0 78 78" aria-hidden="true">
    <circle cx="39" cy="39" r="38" fill="#3b9ad6"/>
    <circle cx="39" cy="39" r="31" fill="none" stroke="#fff" stroke-width="1.5"/>
    <circle cx="39" cy="39" r="17" fill="#fff"/>
  </svg>
  <div class="url-bar">www.brimtek.co.uk/gomanaged</div>
</section>

<section class="side side-back">
  <div class="brand" style="left:38px;top:22px">
    <span class="brand-dot"></span>
    <div>
      <div class="brand-name">BrimTek</div>
      <div class="brand-tag">Helping you work smarter</div>
    </div>
  </div>
  <h2 class="headline headline-services"><span class="plain">OTHER</span> <span class="accent">SERVICES</span></h2>

  <div class="photo photo-meeting" role="img" aria-label="Photo of a business team talking around a meeting table in a brick-walled office"></div>

  <p class="summary">We provide fully accredited Managed IT Support,<br>Cloud and Communications solutions</p>
  <div class="contact-call">
    <div class="call-label">CALL US</div>
    <div class="call-number">
      <svg width="24" height="22" viewBox="0 0 24 22"><path d="M2 8c0-3 4-5 10-5s10 2 10 5l-1 2-4-1V7c-3-1-7-1-10 0v2l-4 1z" fill="#3b9ad6"/><path d="M6 11h12l3 9H3z" fill="#3b9ad6"/><circle cx="12" cy="15" r="2.5" fill="#fff"/></svg>
      03339017462
    </div>
  </div>
  <p class="address">BrimTek Ltd, Unit 8, Calder Court,<br>Hertford, Hertfordshire, SG14 2QX</p>

  <div class="services">
    <div class="service"><div class="service-name">Hosted Desktop</div><p class="service-text">Fully managed Nimbora desktops, securely available from anywhere and any device</p></div>
    <div class="service"><div class="service-name">Managed Telephony</div><p class="service-text">We provide Hosted VoIP telephony services, fully managed with expert technical support</p></div>
    <div class="service"><div class="service-name">Nimbora 365</div><p class="service-text">Fully managed Nimbora 365 migrations, management services and support</p></div>
    <div class="service"><div class="service-name">Managed Internet</div><p class="service-text">Quick and reliable internet services including broadband and leased lines</p></div>
    <div class="service"><div class="service-name">Disaster Recovery</div><p class="service-text">A range of backup and disaster recovery solutions to keep your business data safe and secure</p></div>
  </div>

  <span class="service-icon" style="top:101px"><svg width="18" height="16" viewBox="0 0 18 16" fill="none" stroke="#555" stroke-width="1.4"><rect x="1" y="1" width="16" height="10"/><path d="M9 11v3M5 15h8"/></svg></span>
  <span class="service-icon" style="top:168px"><svg width="16" height="18" viewBox="0 0 16 18" fill="none" stroke="#555" stroke-width="1.4" stroke-linejoin="round"><path d="M4 1l3 4-2 2c1 2 3 4 5 5l2-2 3 3-2 3C7 15 1 9 1 4z"/></svg></span>
  <span class="service-icon" style="top:236px"><svg width="18" height="13" viewBox="0 0 18 13" fill="none" stroke="#555" stroke-width="1.4"><rect x="1" y="1" width="16" height="11"/><path d="M1 1l8 6 8-6"/></svg></span>
  <span class="service-icon" style="top:307px"><svg width="18" height="18" viewBox="0 0 18 18" fill="none" stroke="#555" stroke-width="1.2"><circle cx="9" cy="9" r="8"/><ellipse cx="9" cy="9" rx="3.5" ry="8"/><path d="M1 9h16M2.5 5h13M2.5 13h13"/></svg></span>
  <span class="service-icon" style="top:380px"><svg width="18" height="18" viewBox="0 0 18 18" fill="none" stroke="#555" stroke-width="1.6" stroke-linecap="round"><path d="M15 9a6 6 0 1 1-2-4.5"/><path d="M13 1v4h-4"/></svg></span>

  <div class="url-bar">www.brimtek.co.uk/gomanaged</div>
</section>

</body>
</html>
```